Brookmere Recovery Center Billboard (Addiction / Alcohol / Opioid )

visit www.brookmererecovery-example.com
We are an inpatient treatment center for opioid, alcohol and drug addiction. We are looking to get multiple 12'x25' billboards in our area. Our Phone number is 1-855-CALM-NOW we are located in Elmford Indiana
We pride ourselves on a comfortable medical detox and treat our patients as family.

Target Market(s)

Current Addicts, Addicts family or friends, Factory Workers and Shopvane shoppers

Industry/Entity Type

Health Care

Font styles to use
Sans Serif

Colors
0355a3
3176b5
ffffff

Requirements
Must have
• Logo and Phone number, and Brookmere Recovery
Nice to have
• Ideas?
1.) Addiction hurts more than yourself. (Pic of little girl?)
2.) Just how much are you willing to lose?
3.) Addiction does not define you, You are what you choose to become.
4.) Indiana's most comfortable Detox
5.) Detox in unmatched comfort.
6.) Background could be patient room with logo in upper right
7.) Looking to be able to read easily from road.
Should not have
• Hard to read lettering

```html
<!DOCTYPE html>
<html lang="en">
<head>
<meta charset="UTF-8">
<title>Brookmere Recovery Billboard</title>
<link rel="stylesheet" href="https://fonts.googleapis.com/css2?family=Lato:wght@700;900&display=swap">
<style>
  :root {
    --stage: #2f2f2f;
    --navy: #16245f;
    --sky: #0a9ee0;
    --white: #ffffff;
    --board-top: #f4f8fc;
    --board-mid: #ffffff;
    --board-edge: #d8e6f3;
    --warm-light: #fbe3a3;
    --warm-mid: #e9a25a;
    --warm-dark: #7a4a2e;
  }
  * { margin: 0; padding: 0; box-sizing: border-box; }
  html, body { width: 800px; height: 1200px; overflow: hidden; }
  body {
    background: var(--stage);
    font-family: "Lato", Arial, sans-serif;
    position: relative;
  }
  .billboard {
    position: absolute;
    left: 40px;
    top: 428px;
    width: 720px;
    height: 344px;
    overflow: hidden;
    background:
      radial-gradient(ellipse at 45% 40%, var(--board-mid) 0%, rgba(255,255,255,0) 60%),
      linear-gradient(120deg, var(--board-edge) 0%, var(--board-top) 35%, var(--board-mid) 60%, var(--board-edge) 100%);
    box-shadow: 0 18px 22px -14px rgba(0,0,0,0.7);
  }
  .brand { position: absolute; left: 43px; top: 30px; display: flex; align-items: center; }
  .brand-mark {
    width: 70px; height: 70px; border-radius: 50%;
    background: var(--sky);
    margin-right: 34px;
  }
  .brand-name { color: var(--navy); font-weight: 700; }
  .brand-name .primary { display: block; font-size: 28px; letter-spacing: 1.6px; line-height: 1; }
  .brand-name .secondary { display: block; font-size: 9px; letter-spacing: 17.5px; margin-top: 10px; line-height: 1; color: var(--sky); }
  .headline { position: absolute; left: 41px; top: 126px; color: var(--navy); font-weight: 900; }
  .headline .line { display: block; font-size: 44px; line-height: 1; letter-spacing: -1.2px; }
  .headline .highlight {
    display: inline-block;
    background: var(--navy);
    color: var(--white);
    font-size: 25.5px;
    letter-spacing: -0.7px;
    line-height: 29px;
    padding: 0 8px 0 5px;
    margin: 2px 0 4px;
  }
  .contact { position: absolute; left: 41px; top: 258px; color: var(--sky); font-weight: 900; }
  .contact-row { display: flex; align-items: center; }
  .contact-icon { width: 27px; height: 27px; margin-right: 17px; flex: none; }
  .contact-phone { font-size: 34px; letter-spacing: -0.9px; line-height: 40px; }
  .contact-place { font-size: 25px; font-weight: 700; line-height: 34px; }
  .photo-frame { position: absolute; left: 0; top: 0; }
</style>
</head>
<body>
  <main class="billboard">
    <div class="brand">
      <span class="brand-mark"></span>
      <span class="brand-name">
        <span class="primary">BROOKMERE</span>
        <span class="secondary">RECOVERY</span>
      </span>
    </div>

    <h1 class="headline">
      <span class="line">INDIANA'S</span>
      <span class="highlight">MOST COMFORTABLE</span>
      <span class="line">DETOX</span>
    </h1>

    <div class="contact">
      <div class="contact-row">
        <svg class="contact-icon" viewBox="0 0 28 28" aria-hidden="true">
          <circle cx="14" cy="14" r="14" fill="var(--sky)"/>
          <circle cx="14" cy="14" r="10" fill="none" stroke="#fff" stroke-width="1.6"/>
          <path d="M10.5 8.5c.6-.5 1.3-.4 1.7.2l1 1.5c.3.5.2 1.1-.3 1.5l-.6.5c.5 1.2 1.4 2.2 2.6 2.8l.5-.6c.4-.5 1-.6 1.5-.3l1.5 1c.6.4.7 1.1.2 1.7l-.7.8c-.6.6-1.5.8-2.3.5-2.8-1.1-4.9-3.2-5.9-6-.3-.8-.1-1.7.5-2.3z" fill="#fff"/>
        </svg>
        <span class="contact-phone">1-855-CALM-NOW</span>
      </div>
      <div class="contact-row">
        <svg class="contact-icon" viewBox="0 0 28 28" aria-hidden="true">
          <circle cx="14" cy="14" r="14" fill="var(--sky)"/>
          <path d="M14 6.5a4.5 4.5 0 0 0-4.5 4.5c0 3.3 4.5 8 4.5 8s4.5-4.7 4.5-8A4.5 4.5 0 0 0 14 6.5z" fill="#fff"/>
          <circle cx="14" cy="11" r="1.7" fill="var(--sky)"/>
          <ellipse cx="14" cy="20.5" rx="6" ry="1.8" fill="none" stroke="#fff" stroke-width="1.4"/>
        </svg>
        <span class="contact-place">Elmford Indiana</span>
      </div>
    </div>

    <svg class="photo-frame" width="720" height="344" viewBox="0 0 720 344">
      <defs>
        <radialGradient id="sunset" cx="55%" cy="30%" r="80%">
          <stop offset="0" stop-color="#fff6dc"/>
          <stop offset="0.35" stop-color="var(--warm-light)"/>
          <stop offset="0.65" stop-color="var(--warm-mid)"/>
          <stop offset="1" stop-color="var(--warm-dark)"/>
        </radialGradient>
      </defs>
      <circle cx="544" cy="168" r="152" fill="none" stroke="var(--navy)" stroke-width="6"/>
      <circle cx="544" cy="168" r="141" fill="var(--white)"/>
      <circle cx="544" cy="168" r="138" fill="url(#sunset)" role="img" aria-label="Photo: woman in a white dress and sun hat raising her arms toward a sunset over hills"/>
    </svg>
  </main>
</body>
</html>
```